Strategy and Technology Consulting - Our Story and Values Page

Interior Page design – Our History and Our Values

Our homepage has been designed and we are looking for a design for one of the interior pages. This interior page tells the story of Our History and Our Values

Because the homepage has been designed, we would like this interior page to reflect the design of the homepage without being a mirror image of the homepage.

This site will be implemented in WordPress using the Elementor framework.

Font: Poppins medium and Poppins dark
Illustrations: Our homepage illustrations were designed by “Welmo 1974” on Pixaborne. Compatible original or stock illustrations are welcome. Stock photography is also welcome. Welmo is also available through Welmo Trastek on Folivane

Uploaded Files
• Homepage design – this is the design we will use for our homepage. Contest entries should reflect this basic style but should be distinctly different from the homepage.
• Our History and Our Values – Wireframe – the basic layout of the page we are looking for.
• Our History and Our Values – Word document with the text supporting the wireframe.
• Color Palette – please use colors compatible with the palette attached.

Our Story - timeline
There is a timeline element in the wireframe. The wireframe displays this as a series of chevrons (arrows), but it does not need to be. Creativity in display of the timeline is appreciated.

Our Values
If you look at the Word document, you will see that there are a lot of words on the page. The winning design will present the information in a way that engages the user without overwhelming them with too much to read. For example, they may click on a value and see more information.

Target Market(s)

CIO's and Technology Executives

Number of Pages Required

1 page

Font styles to use
Sans Serif
Other font styles liked:
• Poppin

Requirements
Must have
• A timeline element, all of our values
Nice to have
• Clever timeline display

```html
<!DOCTYPE html>
<html lang="en">
<head>
<meta charset="utf-8">
<title>Vantorra – Our Story and Values</title>
<link href="https://fonts.googleapis.com/css2?family=Poppins:wght@400;500;600;700;800&display=swap" rel="stylesheet">
<style>
:root{
  --blue:#4571a3;
  --pale:#eef2f8;
  --ink:#37445a;
  --text:#3f4656;
  --yellow:#efb71f;
  --slate:#4a5a75;
  --slate-deep:#3e4a5f;
  --grey:#e9e9e9;
}
*{margin:0;padding:0;box-sizing:border-box}
html,body{width:1200px;height:2809px;overflow:hidden;background:var(--grey);font-family:'Poppins',sans-serif;color:var(--text)}
.stage{position:absolute;left:0;top:0;width:1100px;height:2576px;transform:scale(1.090909);transform-origin:0 0}
.page{position:absolute;left:52px;top:45px;width:1000px;height:2475px;background:#fff;box-shadow:0 2px 10px rgba(0,0,0,.12)}
.shapes{position:absolute;left:0;top:0}
.abs{position:absolute}
.brand{font-weight:500;font-size:40px;color:#9aa3b0;letter-spacing:.5px;line-height:1}
.nav{top:72px;display:flex;gap:0;font-size:11px;font-weight:600;color:var(--ink)}
.nav-item{position:absolute;top:73px;font-size:11px;font-weight:600;color:var(--ink);white-space:nowrap}
.nav-item::after{content:"";display:inline-block;width:4px;height:4px;border-right:1.5px solid var(--ink);border-bottom:1.5px solid var(--ink);transform:rotate(45deg);margin-left:5px;position:relative;top:-2px}
.btn{background:var(--yellow);color:#fff;font-weight:700;font-size:10px;border-radius:20px;display:flex;align-items:center;justify-content:center;letter-spacing:.3px}
.page-title{left:125px;top:148px;font-size:38px;font-weight:700;color:var(--ink)}
.year{top:253px;font-size:14px;font-weight:600;color:var(--ink)}
.card{background:#fff;box-shadow:0 1px 6px rgba(0,0,0,.08);padding:24px 18px;font-size:12px;line-height:22px;color:var(--text)}
.card ul{list-style:none}
.card li{position:relative;padding-left:22px}
.card li.tick::before{content:"";position:absolute;left:2px;top:6px;width:10px;height:10px;border-radius:50%;background:var(--yellow)}
.card li.tick::after{content:"";position:absolute;left:5px;top:8px;width:3px;height:5px;border-right:1.5px solid #fff;border-bottom:1.5px solid #fff;transform:rotate(45deg)}
.card li.dash::before{content:"-";position:absolute;left:2px;top:0}
.values-title{left:705px;top:527px;font-size:36px;font-weight:700;color:#fff}
.art{width:128px;height:128px;border-radius:50%;background:radial-gradient(circle at 55% 45%,#dfe7f5 0%,#c9d7ef 55%,#eef2f8 100%)}
.art.warm{background:radial-gradient(circle at 55% 45%,#f6e2a8 0%,#d3dcef 55%,#eef2f8 100%)}
.value-name{font-size:20px;font-weight:700;color:var(--ink);line-height:25px}
.value-text{width:392px;font-size:11.6px;line-height:16.7px;color:var(--text)}
.news{left:166px;top:1929px;width:770px;height:172px;border-radius:86px;background:var(--yellow)}
.news-title{left:234px;top:1974px;font-size:26px;font-weight:800;color:#fff}
.news-sub{left:234px;top:2017px;font-size:13.5px;font-weight:600;color:#fff;line-height:16.5px}
.news-input{left:624px;top:1997px;width:266px;height:38px;border-radius:19px;background:#fff;font-size:11px;color:#8b93a1;display:flex;align-items:center;padding-left:36px}
.news-send{left:853px;top:2000px;width:32px;height:32px;border-radius:50%;background:#8fa6c2}
.foot-h{font-size:17px;font-weight:700;color:#fff}
.foot-list{list-style:none;font-size:11px;color:#fff;line-height:26px}
.foot-list li::before{content:"›";margin-right:7px;font-size:13px}
.contact{font-size:11px;color:#fff;line-height:15px}
.social{width:33px;height:33px;border-radius:50%;background:rgba(255,255,255,.22)}
.copyright{left:52px;top:2472px;width:1000px;height:48px;background:var(--slate-deep);color:#fff;font-size:11.5px;font-weight:500;display:flex;align-items:center;justify-content:center}
.chat{left:997px;top:2451px;width:40px;height:40px;border-radius:50%;background:var(--yellow)}
</style>
</head>
<body>
<div class="stage">
  <div class="page"></div>

  <svg class="shapes" width="1100" height="2576" viewBox="0 0 1100 2576" aria-hidden="true">
    <defs>
      <clipPath id="pageClip"><rect x="52" y="45" width="1000" height="2475"/></clipPath>
      <linearGradient id="footGrad" x1="0" y1="1" x2="1" y2="0">
        <stop offset="0" stop-color="#63799a"/>
        <stop offset=".5" stop-color="#4f6080"/>
        <stop offset="1" stop-color="#44536d"/>
      </linearGradient>
    </defs>
    <g clip-path="url(#pageClip)">
      <!-- pale side curves -->
      <path fill="var(--pale)" d="M52 740 C40 900 60 1000 90 1100 C130 1250 100 1400 52 1530 Z"/>
      <path fill="#fff" d="M52 760 C70 900 80 1000 100 1100 C120 1250 90 1400 52 1500 Z"/>
      <path fill="var(--pale)" d="M52 700 C120 620 220 575 310 575 C340 575 330 585 300 590 C200 610 120 680 52 770 Z"/>
      <path fill="var(--pale)" d="M1052 1430 C990 1520 970 1650 1000 1780 C1015 1830 1040 1850 1052 1850 Z"/>
      <path fill="var(--pale)" d="M1052 565 C980 600 880 630 760 640 L1052 640 Z"/>
      <path fill="#fff" d="M1052 585 C990 615 900 640 800 645 L1052 660 Z"/>
      <!-- main blue wave -->
      <path fill="var(--blue)" d="M52 470 C200 440 320 400 420 410 C520 420 620 395 705 345 L815 320 C900 250 975 215 1052 215 L1052 568 C960 612 830 640 700 636 C560 632 410 565 300 580 C190 595 95 670 52 750 Z"/>
      <!-- timeline -->
      <line x1="151" y1="287" x2="950" y2="287" stroke="#93a7c2" stroke-width="1.5" stroke-dasharray="2 2"/>
      <line x1="815" y1="287" x2="950" y2="287" stroke="#fff" stroke-width="1.5" stroke-dasharray="2 2"/>
      <g fill="#fff" stroke="#8a9ab3" stroke-width="1.2" stroke-dasharray="2 1.5">
        <circle cx="151" cy="287" r="6"/><circle cx="376" cy="287" r="6"/><circle cx="473" cy="287" r="6"/>
        <circle cx="629" cy="287" r="6"/><circle cx="731" cy="287" r="6"/>
      </g>
      <circle cx="950" cy="287" r="6" fill="var(--blue)" stroke="#fff" stroke-width="1.2" stroke-dasharray="2 1.5"/>
      <!-- footer waves -->
      <path fill="#d9dde4" d="M52 1990 C200 2040 260 2140 420 2165 C560 2185 680 2120 800 2160 C900 2195 990 2100 1052 2070 L1052 2520 L52 2520 Z"/>
      <path fill="url(#footGrad)" d="M52 1950 C160 1980 240 2090 380 2140 C520 2185 650 2110 790 2150 C900 2180 980 2090 1052 2045 L1052 2520 L52 2520 Z"/>
    </g>
  </svg>

  <!-- header -->
  <div class="abs brand" style="left:130px;top:60px">Vantorra</div>
  <svg class="abs" style="left:505px;top:73px" width="13" height="12" viewBox="0 0 13 12" aria-hidden="true"><path d="M6.5 0 L13 6 H11 V12 H8 V8 H5 V12 H2 V6 H0 Z" fill="#9aa3b0"/></svg>
  <div class="nav-item" style="left:541px">ABOUT US</div>
  <div class="nav-item" style="left:625px">SERVICES</div>
  <div class="nav-item" style="left:706px">INSIGHTS</div>
  <div class="nav-item" style="left:786px">JOIN US</div>
  <div class="abs btn" style="left:868px;top:63px;width:109px;height:32px">CONTACT US</div>

  <!-- our story -->
  <h1 class="abs page-title">Our Story</h1>
  <div class="abs year" style="left:136px">2017</div>
  <div class="abs year" style="left:360px">2019</div>
  <div class="abs year" style="left:456px">2020</div>
  <div class="abs year" style="left:614px">2021</div>
  <div class="abs year" style="left:714px">2022</div>
  <div class="abs year" style="left:921px;color:#fff">Onward</div>

  <div class="abs card" style="left:125px;top:320px;width:273px;height:133px">
    <ul>
      <li class="tick">Growth Strategy Focus</li>
      <li class="tick">Consistent, Modest Growth</li>
      <li class="tick">Preliminary Focus on Technology</li>
      <li class="tick">Eureka! Implementing strategy is hard</li>
    </ul>
  </div>
  <div class="abs card" style="left:451px;top:320px;width:201px;height:133px">
    <ul>
      <li class="tick">Pandemic Pauses Growth</li>
      <li class="tick">Rethinking:</li>
      <li class="dash">the business model</li>
      <li class="dash">the delivery model</li>
    </ul>
  </div>
  <div class="abs card" style="left:705px;top:320px;width:272px;height:133px;padding-top:28px;line-height:17px">
    <ul>
      <li class="tick" style="margin-bottom:5px">Leadership Team for Focus on Essential Areas</li>
      <li class="tick" style="margin-bottom:5px">Rapid Growth</li>
      <li class="tick">Customer Success</li>
    </ul>
  </div>

  <!-- our values -->
  <h2 class="abs values-title">Our Values</h2>

  <div class="abs art" style="left:125px;top:697px" role="img" aria-label="Illustration of a diverse group of people in front of a globe"></div>
  <h3 class="abs value-name" style="left:285px;top:735px">The Value of Every<br>Human. Regardless.</h3>
  <p class="abs value-text" style="left:125px;top:845px">Each person's unique experiences and perspectives add vibrant hues to the tapestry of our shared existence. In a world where diversity paints the canvas of humanity, true beauty is found in recognizing the inherent and incalculable value of every human being.</p>

  <div class="abs art warm" style="left:588px;top:697px" role="img" aria-label="Illustration of two people joining puzzle pieces above a light bulb"></div>
  <h3 class="abs value-name" style="left:748px;top:747px">Collaboration</h3>
  <p class="abs value-text" style="left:588px;top:845px">Collaboration in work transforms individual endeavors into symphonies of collective achievement. Through collaboration, diverse talents converge, fostering a rich exchange of ideas that amplifies creativity, accelerates progress, and brings forth solutions beyond sin…</p>

  <div class="abs art" style="left:125px;top:977px" role="img" aria-label="Illustration of people beside a monitor showing a target and charts"></div>
  <h3 class="abs value-name" style="left:282px;top:1027px">Tenacity</h3>
  <p class="abs value-text" style="left:125px;top:1125px">Tenacity is the unwavering anchor that keeps us grounded amidst adversity, propelling us forward when faced with obstacles. The resilience to persist, adapt, and learn from setbacks leads to the mastery of skills and the fulfillment of ambitious goals.</p>

  <div class="abs art warm" style="left:588px;top:977px" role="img" aria-label="Illustration of people climbing steps toward a flag"></div>
  <h3 class="abs value-name" style="left:748px;top:1027px">Excellence</h3>
  <p class="abs value-text" style="left:588px;top:1125px">Excellence isn't a destination; it's a continuous journey of refinement and growth. Striving for excellence cultivates a culture of continuous improvement, fostering innovation, credibility, and a lasting impact that resonates far beyond the immediate task.</p>

  <div class="abs art warm" style="left:125px;top:1255px" role="img" aria-label="Illustration of a rocket launching with people celebrating"></div>
  <h3 class="abs value-name" style="left:292px;top:1306px">Passion</h3>
  <p class="abs value-text" style="left:125px;top:1404px">Passion infuses our work with energy, transforming routine tasks into opportunities for creativity and innovation. Fueled by passion, individuals become unstoppable forces, driven to overcome challenges and achieve remarkable outcomes that benefit them and inspire those around them</p>

  <div class="abs art" style="left:588px;top:1255px" role="img" aria-label="Illustration of a person beside a brain with a light bulb"></div>
  <h3 class="abs value-name" style="left:749px;top:1306px">Solution Mindset</h3>
  <p class="abs value-text" style="left:588px;top:1404px">A solution mindset is the compass that directs our focus from problems to possibilities. It empowers us to navigate challenges with a proactive mindset, igniting a journey of exploration and innovation that not only resolves issues but also paves the way for continuous growth and success.</p>

  <div class="abs art" style="left:125px;top:1553px" role="img" aria-label="Illustration of people around a tablet with gears and social icons"></div>
  <h3 class="abs value-name" style="left:285px;top:1602px">Generosity</h3>
  <p class="abs value-text" style="left:125px;top:1720px">Generosity creates a virtuous cycle of goodwill, fostering a sense of unity and shared purpose among colleagues. By freely sharing knowledge, support, and resources, we uplift those around us and contribute to a collaborative environment where collective achievements flourish.</p>

  <!-- newsletter -->
  <div class="abs news"></div>
  <h2 class="abs news-title">Subscribe Our Newsletter</h2>
  <p class="abs news-sub">Subscribe our newsletter to receive the latest news<br>and exclusive offers every week, No spam.</p>
  <div class="abs news-input">
    <svg style="position:absolute;left:18px;top:14px" width="12" height="9" viewBox="0 0 12 9" aria-hidden="true"><rect width="12" height="9" rx="1" fill="#a3abb8"/><path d="M0 1 L6 5 L12 1" stroke="#fff" fill="none"/></svg>
    Enter email address
  </div>
  <div class="abs news-send">
    <svg style="position:absolute;left:9px;top:9px" width="14" height="14" viewBox="0 0 14 14" aria-hidden="true"><path d="M13 1 L1 6 L6 8 L8 13 Z" fill="#fff"/></svg>
  </div>

  <!-- footer -->
  <div class="abs brand" style="left:152px;top:2252px;font-size:52px;color:#fff">Vantorra</div>
  <div class="abs social" style="left:200px;top:2317px"></div>
  <div class="abs social" style="left:242px;top:2317px"></div>
  <div class="abs social" style="left:285px;top:2317px"></div>
  <div class="abs social" style="left:326px;top:2317px"></div>
  <div class="abs btn" style="left:231px;top:2371px;width:109px;height:30px">CONTACT US</div>

  <h4 class="abs foot-h" style="left:461px;top:2230px">Quick links</h4>
  <ul class="abs foot-list" style="left:461px;top:2267px">
    <li>Home</li><li>About Us</li><li>Services</li><li>Insights</li><li>Join Us</li><li>Contact Us</li>
  </ul>
  <h4 class="abs foot-h" style="left:608px;top:2230px">Our Services</h4>
  <ul class="abs foot-list" style="left:608px;top:2267px">
    <li>Business Transformation</li><li>ERP Implementations</li><li>ERP Solutions</li><li>BI and Data</li><li>Building the Right Team...</li>
  </ul>
  <h4 class="abs foot-h" style="left:801px;top:2230px">Contact info</h4>
  <svg class="abs" style="left:801px;top:2275px" width="12" height="9" viewBox="0 0 12 9" aria-hidden="true"><rect width="12" height="9" rx="1" fill="var(--yellow)"/><path d="M0 1 L6 5 L12 1" stroke="#4f6080" fill="none"/></svg>
  <div class="abs contact" style="left:820px;top:2272px">Email:<br>hello@northquill.com</div>
  <svg class="abs" style="left:801px;top:2318px" width="12" height="12" viewBox="0 0 12 12" aria-hidden="true"><path d="M2 0 L4.5 2.5 L3 4.5 C4 6.5 5.5 8 7.5 9 L9.5 7.5 L12 10 L10 12 C5 11 1 7 0 2 Z" fill="var(--yellow)"/></svg>
  <div class="abs contact" style="left:820px;top:2317px">Phone:<br>+44 100 555 0199</div>
  <svg class="abs" style="left:803px;top:2362px" width="10" height="14" viewBox="0 0 10 14" aria-hidden="true"><path d="M5 0 C8 0 10 2 10 5 C10 8 5 14 5 14 C5 14 0 8 0 5 C0 2 2 0 5 0 Z" fill="var(--yellow)"/><circle cx="5" cy="5" r="2" fill="#4f6080"/></svg>
  <div class="abs contact" style="left:820px;top:2362px">Location:<br>Some address line goes<br>here city name</div>

  <div class="abs copyright">© Vantorra Design 2023, All Rights Reserved</div>
  <div class="abs chat">
    <svg style="position:absolute;left:10px;top:11px" width="20" height="18" viewBox="0 0 20 18" aria-hidden="true"><path d="M10 0 C16 0 20 3.5 20 8 C20 12.5 16 16 10 16 L4 18 L5 14 C2 12.5 0 10.5 0 8 C0 3.5 4 0 10 0 Z" fill="#fff"/><circle cx="6" cy="8" r="1.4" fill="var(--yellow)"/><circle cx="10" cy="8" r="1.4" fill="var(--yellow)"/><circle cx="14" cy="8" r="1.4" fill="var(--yellow)"/></svg>
  </div>
</div>
</body>
</html>
```